Harvest Gathering event flyer

I would like a church event flyer designed. The event is called "HARVEST GATHERING 2018". I am looking for a professional, yet catchy design that uses our brand colors and logo creatively while communicating key information of the event effectively.

1. The logo is attached in two color formats. The designer has the choice to use them as he/she want.

2. The location of the event is: Lindqvist Community Center, 482 Tamsworth Street, Portland, ME 04102
3. Time and date of event. The designer can organize and format the date and time as he/she pleases.
December 28th, 29th @ 7:00PM
December 30th @ 10:00AM
4. The topic of the event is "Tongues of fire". The designer is free to use this phrase as he/she pleases to create a good composition.
5. Speaker: Prophet Marcus Obuya
6. Contact information: contact@cedarbrookfellowship.org - Telephone number: 207 555 0148

7. I would also like the following three words on the flyer. These words describe the focus of the event: FIRE, REVIVAL, PROPHETIC

```html
<!DOCTYPE html>
<html lang="en">
<head>
<meta charset="utf-8">
<title>Harvest Gathering 2018 – Tongues of Fire</title>
<link href="https://fonts.googleapis.com/css2?family=Cinzel:wght@400;600;700&family=Yellowtail&family=Oswald:wght@400&display=swap" rel="stylesheet">
<style>
  :root{
    --page:#ffffff;
    --navy-deep:#141c2b;
    --navy:#1f3b5e;
    --navy-mid:#24426a;
    --orange:#f7941d;
    --tan:#c98a4a;
    --white:#ffffff;
    --grey:#a4afc2;
    --rule:#b67a3f;
  }
  *{margin:0;padding:0;box-sizing:border-box;}
  html,body{width:1200px;height:1200px;overflow:hidden;background:var(--page);}
  .flyer{
    position:absolute;left:198px;top:30px;
    width:885px;height:1255px;
    transform:scale(0.908);transform-origin:top left;
    background:linear-gradient(180deg,var(--navy-deep) 0%,#1b2a42 40%,var(--navy-mid) 75%,var(--navy) 100%);
    overflow:hidden;
    font-family:"Cinzel",serif;
    color:var(--white);
    text-align:center;
  }
  .hero-photo{
    position:absolute;left:0;top:0;width:885px;height:600px;
    background:
      radial-gradient(ellipse 260px 200px at 760px 300px,rgba(255,190,90,.85),rgba(230,120,30,.35) 55%,transparent 80%),
      radial-gradient(ellipse 340px 260px at 520px 300px,#8a6a58 0%,#5c4336 45%,transparent 85%),
      radial-gradient(ellipse 420px 320px at 540px 150px,#b38e78 0%,transparent 75%),
      linear-gradient(180deg,#15161c 0%,#1c2232 70%,rgba(27,42,66,0) 100%);
  }
  .brand{
    position:absolute;left:80px;top:105px;
    display:flex;align-items:center;gap:14px;
  }
  .brand-dot{width:26px;height:26px;border-radius:50%;background:var(--orange);}
  .brand-name{font-size:58px;font-weight:400;color:var(--white);letter-spacing:1px;line-height:1;}
  .event-name{
    position:absolute;left:0;width:100%;top:520px;
    font-size:60px;line-height:1;white-space:nowrap;
  }
  .event-name .script{font-family:"Yellowtail",cursive;}
  .event-name .year{font-family:"Cinzel",serif;font-size:56px;margin-left:10px;}
  .topic-small{
    position:absolute;left:0;width:100%;top:582px;
    font-size:98px;font-weight:600;color:var(--tan);line-height:1;letter-spacing:1px;
  }
  .topic-large{
    position:absolute;left:0;width:100%;top:648px;
    font-size:272px;font-weight:600;color:var(--orange);line-height:1;letter-spacing:10px;
  }
  .glow{
    position:absolute;left:60px;width:765px;height:2px;
    background:linear-gradient(90deg,transparent,rgba(255,210,140,.9) 50%,transparent);
  }
  .glow.upper{top:900px;}
  .glow.lower{top:962px;}
  .focus{
    position:absolute;left:0;width:100%;top:908px;
    font-size:46px;font-weight:600;letter-spacing:1px;line-height:1.1;
  }
  .schedule{
    position:absolute;left:0;width:100%;top:993px;
    font-family:"Oswald",sans-serif;font-size:30px;color:var(--grey);letter-spacing:.3px;
  }
  .venue{
    position:absolute;left:0;width:100%;top:1033px;
    font-size:29px;color:var(--grey);letter-spacing:2px;
  }
  .rule{position:absolute;left:115px;width:650px;height:1px;background:var(--rule);}
  .rule.top{top:1077px;}
  .rule.bottom{top:1129px;}
  .speaker{
    position:absolute;left:0;width:100%;top:1083px;
    font-size:33px;color:var(--tan);letter-spacing:2px;
  }
  .contact{
    position:absolute;left:0;width:100%;top:1158px;
    display:flex;justify-content:center;align-items:center;gap:12px;
    font-size:24px;color:var(--white);
  }
  .contact .item{display:flex;align-items:center;gap:8px;}
  .contact .phone{font-size:26px;}
  .contact svg{width:28px;height:28px;}
</style>
</head>
<body>
  <main class="flyer">
    <div class="hero-photo" role="img" aria-label="Close-up photo of an open mouth with a tongue engulfed in flames"></div>

    <div class="brand">
      <span class="brand-dot"></span>
      <span class="brand-name">KELTRA</span>
    </div>

    <h2 class="event-name"><span class="script">Harvest Gathering</span><span class="year">2018</span></h2>
    <h1>
      <span class="topic-small">TONGUES OF</span>
      <span class="topic-large">FIRE</span>
    </h1>

    <div class="glow upper"></div>
    <p class="focus">FIRE, REVIVAL, PROPHETIC</p>
    <div class="glow lower"></div>

    <p class="schedule">DECEMBER 28TH, 29TH @ 7:00PM &nbsp;|&nbsp; DECEMBER 30TH @ 10:00AM</p>
    <p class="venue">482 TAMSWORTH STREET, PORTLAND, ME 04102</p>

    <div class="rule top"></div>
    <p class="speaker">SPEAKER: PROPHET MARCUS OBUYA</p>
    <div class="rule bottom"></div>

    <div class="contact">
      <span class="item phone">
        <svg viewBox="0 0 28 28" aria-hidden="true"><circle cx="14" cy="14" r="12.5" fill="none" stroke="#f7941d" stroke-width="1.6"/><path d="M10 8.5l2 .2 1 3-1.4 1.2a8 8 0 0 0 3.5 3.5l1.2-1.4 3 1 .2 2c-.4 1-1.4 1.5-2.4 1.4C12 18.8 9.2 16 8.6 10.9c-.1-1 .4-2 1.4-2.4z" fill="#f7941d"/></svg>
        207 555 0148
      </span>
      <span class="item">
        <svg viewBox="0 0 28 28" aria-hidden="true"><circle cx="14" cy="14" r="12.5" fill="none" stroke="#f7941d" stroke-width="1.6"/><rect x="8" y="9.5" width="12" height="9" rx="1" fill="none" stroke="#f7941d" stroke-width="1.5"/><path d="M8.5 10.5l5.5 4.2 5.5-4.2" fill="none" stroke="#f7941d" stroke-width="1.5"/></svg>
        CONTACT@CEDARBROOKFELLOWSHIP.ORG
      </span>
    </div>
  </main>
</body>
</html>
```